Graphics for FABRIX NORTH 2014

We need to create 3 product introduction displays for semiconductor trade show. It includes company logo on top, product name and application, product picture, and 2-3 bullet points to describe product features. Attached please find my image.
Required format is higher than 300 dpi at a size of 8 x 10" (vertically long) and file type should be EPS, TIF, or JPG in order of preference.
I need 3 graphics, one per product.

Reason: I need to see more to pick up the most suitable one.

Target Market(s)

High-tech semiconductor manufacturing companies such like Varso, QRT.

Industry/Entity Type

Trade

Font styles to use
Serif

Colors

Designer to choose colors to be used in the design.

Requirements
Must have
• 3 pages, one per product with same format/background
Should not have
• should not have any fancy cartoons. Must be proffesional style.

```html
<!DOCTYPE html>
<html lang="en">
<head>
<meta charset="utf-8">
<title>Veltrane Technology Inc. – KORVEX-H3PO4 Reclaim System</title>
<link rel="stylesheet" href="https://fonts.googleapis.com/css2?family=Montserrat:wght@300;700&family=Roboto+Condensed:wght@400;700&family=Quicksand:wght@300&family=Arimo&display=swap">
<style>
  :root {
    --paper: #fbfbfb;
    --teal: #3f9aa0;
    --teal-text: #3d8d93;
    --orange: #e97843;
    --white: #ffffff;
    --sky-top: #1c5cc0;
    --sky-mid: #3f8ddf;
    --sky-low: #79aee6;
    --buildings: #7d8a94;
    --street: #4a4f55;
    --bullet-1: #ee9a9f;
    --bullet-2: #1b8fd6;
    --bullet-3: #655b99;
  }
  * { margin: 0; padding: 0; box-sizing: border-box; }
  html, body { width: 928px; height: 1200px; overflow: hidden; background: var(--paper); }
  .sheet { position: relative; width: 928px; height: 1200px; background: var(--paper); }
  .frame { position: absolute; inset: 0; }
  .year {
    position: absolute; left: 51px; top: 136px;
    font-family: "Quicksand", sans-serif; font-weight: 300;
    font-size: 56px; letter-spacing: 7px; color: var(--white); line-height: 1;
  }
  .company {
    position: absolute; right: 75px; top: 124px;
    font-family: "Roboto Condensed", sans-serif; font-weight: 400;
    font-size: 43px; color: var(--teal-text); line-height: 1;
  }
  .product { position: absolute; right: 75px; top: 216px; text-align: right; color: var(--white); font-family: "Montserrat", sans-serif; }
  .product-code { font-weight: 300; font-size: 33px; line-height: 1; }
  .product-name { font-weight: 700; font-size: 40px; line-height: 1; margin-top: 12px; }
  .features { position: absolute; left: 67px; top: 980px; }
  .features-title {
    font-family: "Roboto Condensed", sans-serif; font-weight: 700;
    font-size: 29px; color: var(--teal-text); line-height: 1; margin-bottom: 14px;
  }
  .feature-list { list-style: none; font-family: "Arimo", sans-serif; font-size: 24px; line-height: 31px; }
  .feature-list li::before { content: "»"; margin-right: 14px; }
  .feature-list .f1 { color: var(--bullet-1); }
  .feature-list .f2 { color: var(--bullet-2); }
  .feature-list .f3 { color: var(--bullet-3); }
</style>
</head>
<body>
<div class="sheet">
  <svg class="frame" width="928" height="1200" viewBox="0 0 928 1200">
    <defs>
      <linearGradient id="streetScene" x1="0" y1="0" x2="0" y2="1">
        <stop offset="0" stop-color="var(--sky-top)"/>
        <stop offset="0.45" stop-color="var(--sky-mid)"/>
        <stop offset="0.68" stop-color="var(--sky-low)"/>
        <stop offset="0.85" stop-color="var(--buildings)"/>
        <stop offset="1" stop-color="var(--street)"/>
      </linearGradient>
    </defs>
    <rect class="side-rail" x="0" y="0" width="35" height="1200" fill="var(--teal)"/>
    <polygon class="year-panel" points="0,137 205,137 258,878 0,878" fill="var(--orange)"/>
    <polygon class="product-photo" role="img" aria-label="Product photo area: palm-lined city boulevard with office buildings under a clear blue sky"
             points="221,197 928,197 928,940 275,940" fill="url(#streetScene)"/>
    <rect class="photo-band" x="272" y="877" width="656" height="28" fill="var(--orange)"/>
    <rect class="foot-line" x="35" y="1192" width="893" height="5" fill="var(--orange)"/>
  </svg>

  <div class="year">2014</div>
  <div class="company">Veltrane Technology Inc.</div>
  <div class="product">
    <div class="product-code">KORVEX-H3PO4</div>
    <div class="product-name">Reclaim System</div>
  </div>

  <div class="features">
    <h2 class="features-title">Product Features:</h2>
    <ul class="feature-list">
      <li class="f1">ABC</li>
      <li class="f2">DEF</li>
      <li class="f3">XYZ</li>
    </ul>
  </div>
</div>
</body>
</html>
```